" Somos a Casa Lumiar, uma empresa que atua no vareja em Fortaleza - CE e já estamos a mais de 20 anos no ramo. Nós vendemos produtos gastronômicos de marcas como: tavares, gelmar, brixley... para restaurantes, padaria, confeitarias, escolas de culinárias, cozinhas industriais em geral. Oferecemos atendimento atualmente em loja física principalmente presencial, e por ligação, além de termos um site(não vendemos por ele). A ideia é que dentro de 2 meses trabalhemos apenas com atendimento externo, por ligação e por ecommerce, ou seja, de portas fechadas. O objetivo é diminuir a passividade do setor comercial e aumentar a personalização do nosso atendimento para os maiores clientes do mercado. Somos umas das maiores empresas do ramo em Fortaleza e provavelmente a melhor em questão de atendimento ao cliente. Nossa identidade é: * Visão: * A Casa Lumiar como a maior fornecedora de equipamentos de ponta para os principais negócios gastronômicos do Ceará. E como principal parceira no ceará dos pequenos negócios da área gastronômica. * Missão: * Nós ajudamos empreendedores do setor gastronômico a equiparem seus negócios com soluções em automação e produção. * Valores: * Excelência: Fazer tudo da melhor maneira possível. * Simplicidade. * Foco no próximo: Satisfazer a *necessidade* do outro, se preciso antes da própria necessidade. * Integridade: Fazer tudo de forma correta e as claras, com transparência e honestidade. * Inovação: Buscar pelo novo e por fazer diferente e melhor aquilo que já se faz. * Sucesso: Desenvolver a plenitude e a paz interior e impactar a exterior com atitudes. * Responsabilidade: Responder pelas próprias atitudes, tomar para si seus deveres e lidar com suas consequências. "

```html
<!DOCTYPE html>
<html lang="pt-BR">
<head>
<meta charset="utf-8">
<title>Casa Lumiar — Supermercados</title>
<link href="https://fonts.googleapis.com/css2?family=Arimo:wght@400;700&display=swap" rel="stylesheet">
<style>
  :root {
    --green-dark: #0f4f22;
    --green: #1d6e31;
    --green-light: #2f8a41;
    --gold: #c9a04a;
    --gold-light: #e9cf8a;
    --white: #ffffff;
    --page: #ffffff;
  }
  * { box-sizing: border-box; margin: 0; padding: 0; }
  html, body {
    width: 1200px; height: 1200px; overflow: hidden;
    background: var(--page);
    font-family: "Arimo", Arial, sans-serif;
  }
  .flyer {
    position: absolute; left: 144px; top: 0;
    width: 912px; height: 1200px;
    overflow: hidden;
    background: var(--green);
  }
  .top-rule {
    position: absolute; left: 0; top: 0; width: 100%; height: 14px;
    background: linear-gradient(90deg, var(--gold), var(--gold-light), var(--gold));
  }
  .hero-photo {
    position: absolute; left: 0; top: 14px; width: 100%; height: 730px;
    background:
      radial-gradient(ellipse at 70% 45%, #f3d9b8 0%, rgba(243,217,184,0) 45%),
      radial-gradient(ellipse at 20% 70%, #8c3a2a 0%, rgba(140,58,42,0) 35%),
      linear-gradient(160deg, #f2e2c8 0%, #d8b08a 40%, #a9724e 75%, #7c4a33 100%);
  }
  .brand {
    position: absolute; left: 30px; top: 70px;
    display: flex; align-items: center; gap: 14px;
  }
  .brand-dot {
    width: 54px; height: 54px; border-radius: 50%;
    background: var(--green);
  }
  .brand-text { display: flex; flex-direction: column; }
  .brand-name {
    font-size: 38px; font-weight: 700; color: var(--green);
    letter-spacing: 0.5px;
  }
  .brand-tagline {
    font-size: 13px; color: var(--green); margin-top: 4px;
  }
  .segment-tag {
    position: absolute; left: 450px; top: 616px; width: 470px; height: 76px;
  }
  .segment-tag span {
    position: absolute; left: 0; top: 0; width: 100%; height: 100%;
    display: flex; align-items: center; justify-content: center;
    padding-left: 40px;
    font-size: 40px; font-weight: 700; color: var(--white);
    letter-spacing: 0.5px;
  }
  .offer-panel {
    position: absolute; left: 0; top: 744px; width: 100%; height: 432px;
    background: linear-gradient(170deg, var(--green-light) 0%, var(--green) 45%, var(--green-dark) 100%);
    border-top: 6px solid var(--gold);
    padding: 36px 0 0 46px;
    color: var(--white);
  }
  .offer-lead { font-size: 34px; line-height: 1.15; }
  .offer-lead strong { font-weight: 700; font-size: 38px; }
  .offer-headline {
    font-size: 44px; font-weight: 700; line-height: 1.1; letter-spacing: 0.3px;
  }
  .offer-sub { font-size: 32px; line-height: 1.2; }
  .terms { margin-top: 44px; }
  .terms-title {
    font-size: 31px; font-weight: 700; margin-bottom: 12px;
  }
  .terms-list { list-style: none; }
  .terms-list li {
    font-size: 22px; font-weight: 700; line-height: 33px;
  }
  .bottom-rule {
    position: absolute; left: 0; bottom: 0; width: 100%; height: 24px;
    background: linear-gradient(90deg, var(--gold), var(--gold-light), var(--gold));
  }
</style>
</head>
<body>
  <main class="flyer">
    <div class="top-rule"></div>
    <div class="hero-photo" role="img" aria-label="Fotografia de um caixa de supermercado: operadora sorridente atendendo clientes com cesta de compras"></div>

    <div class="brand">
      <div class="brand-dot"></div>
      <div class="brand-text">
        <div class="brand-name">Casa Lumiar</div>
        <div class="brand-tagline">Equipamentos para o seu negócio</div>
      </div>
    </div>

    <div class="segment-tag">
      <svg width="470" height="76" viewBox="0 0 470 76">
        <polygon points="30,2 470,2 470,74 0,74" fill="#1d6e31" stroke="#c9a04a" stroke-width="4"/>
      </svg>
      <span>SUPERMERCADOS</span>
    </div>

    <section class="offer-panel">
      <p class="offer-lead">NOSSO <strong>OBJETIVO</strong> E FORNECER</p>
      <p class="offer-headline">ATENDIMENTO PERSONALIZADO</p>
      <p class="offer-sub">e excelente para o cliente</p>
      <div class="terms">
        <p class="terms-title">Conheça nossas condiçoes comerciais</p>
        <ul class="terms-list">
          <li>Conheça nossas condiçoes comerciais</li>
          <li>Conheça nossas condiçoes comerciais</li>
          <li>Conheça nossas condiçoes comerciais</li>
          <li>Conheça nossas condiçoes comerciais</li>
        </ul>
      </div>
    </section>
    <div class="bottom-rule"></div>
  </main>
</body>
</html>
```